Brightwire Hollow Business cards

one side I would like my logo (uploaded) and the other side I want my details. I'm an electrician in sydney. The logo side I'm happy with just a white background and our logo in the middle.

Details for other side
24/7 Sydney Electrician
Marcus Pell
0431 587 219
marcus@brightwirehollow.com.au
brightwirehollow.com.au
icons for facebook, instagram, linked in

Industry/Entity Type

electrician

Contact Information for Business Card

company info

```html
<!DOCTYPE html>
<html lang="en">
<head>
<meta charset="utf-8">
<title>Brightwire Hollow – Business Cards</title>
<link href="https://fonts.googleapis.com/css2?family=Exo+2:wght@500;600;700&display=swap" rel="stylesheet">
<style>
  :root {
    --backdrop: #262626;
    --card: #1f1f1f;
    --card-back: #222222;
    --red: #e2342a;
    --white: #f2f2f2;
    --mark: #303030;
  }
  * { margin: 0; padding: 0; box-sizing: border-box; }
  html, body { width: 1200px; height: 901px; overflow: hidden; }
  body {
    background: var(--backdrop);
    font-family: "Exo 2", sans-serif;
    position: relative;
  }
  .card {
    position: absolute;
    top: 317px;
    width: 470px;
    height: 269px;
    border-radius: 12px;
    box-shadow: 0 4px 10px rgba(0,0,0,.45);
  }
  .card-front { left: 117px; background: var(--card); }
  .card-back { left: 613px; background: var(--card-back); display: flex; align-items: center; justify-content: center; }

  .wordmark {
    position: absolute;
    left: 33px;
    top: 103px;
    width: 184px;
    color: var(--red);
    font-weight: 700;
    font-size: 25px;
    line-height: 27px;
    letter-spacing: 0.5px;
    text-transform: uppercase;
  }
  .divider {
    position: absolute;
    left: 236px;
    top: 84px;
    width: 1.5px;
    height: 98px;
    background: var(--red);
  }
  .details { position: absolute; left: 253px; top: 79px; }
  .person-name {
    color: var(--red);
    font-weight: 600;
    font-size: 17.5px;
    text-transform: uppercase;
    line-height: 22px;
  }
  .role { color: var(--white); font-weight: 500; font-size: 13px; line-height: 17px; }
  .contacts { list-style: none; margin-top: 14px; }
  .contacts li {
    display: flex; align-items: center; gap: 6px;
    color: var(--white); font-weight: 500; font-size: 12.5px; line-height: 18px;
  }
  .contacts svg { width: 11px; height: 11px; flex: none; }
  .social {
    position: absolute; left: 200px; top: 235px;
    display: flex; gap: 10px;
  }
  .social span { width: 16px; height: 16px; border-radius: 50%; background: var(--red); }

  .back-name {
    color: var(--mark);
    font-weight: 700;
    font-size: 26px;
    text-transform: uppercase;
    letter-spacing: 1px;
  }
</style>
</head>
<body>
  <section class="card card-front">
    <div class="wordmark">Brightwire<br>Hollow</div>
    <div class="divider"></div>
    <div class="details">
      <div class="person-name">Marcus Pell</div>
      <div class="role">24/7 Sydney Electrician</div>
      <ul class="contacts">
        <li>
          <svg viewBox="0 0 24 24" fill="var(--red)"><path d="M6.6 10.8a15.1 15.1 0 0 0 6.6 6.6l2.2-2.2a1 1 0 0 1 1-.25 11.4 11.4 0 0 0 3.6.57 1 1 0 0 1 1 1V20a1 1 0 0 1-1 1A17 17 0 0 1 3 4a1 1 0 0 1 1-1h3.5a1 1 0 0 1 1 1c0 1.25.2 2.45.57 3.57a1 1 0 0 1-.25 1z"/></svg>
          0431 587 219
        </li>
        <li>
          <svg viewBox="0 0 24 24" fill="var(--red)"><path d="M2 5h20v14H2z" opacity=".0"/><path d="M2 5h20v2l-10 6L2 7z"/><path d="M2 9l10 6 10-6v10H2z"/></svg>
          marcus@brightwirehollow.com.au
        </li>
        <li>
          <svg viewBox="0 0 24 24" fill="none" stroke="var(--red)" stroke-width="2"><circle cx="12" cy="12" r="9.5"/><ellipse cx="12" cy="12" rx="4" ry="9.5"/><path d="M2.5 12h19M4 7h16M4 17h16"/></svg>
          brightwirehollow.com.au
        </li>
      </ul>
    </div>
    <div class="social" aria-label="Social media links">
      <span></span><span></span><span></span>
    </div>
  </section>

  <section class="card card-back">
    <div class="back-name">Brightwire Hollow</div>
  </section>
</body>
</html>
```